Software Consulting Business Needs a Powerpoint Design

We need a powerpoint template design for a software consulting company called Tessel7, that we can use for a corporate overview presentation.

Our website/logo can be found at www.tessel7-demo.net which should give you a good idea of our color scheme.

Here is a link to a zip file with the logos in AI format:

http://www.tessel7-demo.net/logo/T7_Logo_Illustrator.zip

Here is a link to the Din font:

http://www.tessel7-demo.net/logo/Din.zip

Sorry for delay. I was on vacation. A decision will be made by end of the week. Thanks!

Software

```html
<!DOCTYPE html>
<html lang="en">
<head>
<meta charset="utf-8">
<title>Strategy and Our Vision – Tessel7</title>
<link rel="stylesheet" href="https://fonts.googleapis.com/css2?family=Barlow:wght@300;400;500;600&display=swap">
<style>
  :root {
    --page-bg: #f2f2f2;
    --sidebar: #33404f;
    --band-red: #f15640;
    --band-red-light: #f2665a;
    --band-fold: #b8452f;
    --body-text: #4d4b3c;
    --divider: #f08a70;
    --navy: #25303e;
    --coral: #f0533a;
    --olive: #958a55;
    --core: #f6f5f0;
    --label: #2a3545;
    --white: #ffffff;
  }
  * { margin: 0; padding: 0; box-sizing: border-box; }
  html, body { width: 1200px; height: 900px; overflow: hidden; }
  body { background: var(--page-bg); font-family: "Barlow", Arial, sans-serif; }
  .slide { position: relative; width: 1200px; height: 900px; overflow: hidden; background: var(--page-bg); }
  .sidebar { position: absolute; left: 0; top: 0; width: 180px; height: 900px; background: var(--sidebar); }
  .brand { position: absolute; left: 16px; top: 336px; display: flex; align-items: center; gap: 10px;
    color: var(--white); font-weight: 500; font-size: 27px; letter-spacing: 1px; }
  .brand-mark { width: 14px; height: 14px; background: var(--white); }
  .band-tab { position: absolute; left: 0; top: 38px; width: 176px; height: 70px; background: var(--band-red-light); }
  .band-fold { position: absolute; left: 172px; top: 100px; width: 8px; height: 8px; background: var(--band-fold); }
  .title-band { position: absolute; left: 172px; top: 30px; width: 1028px; height: 72px;
    background: linear-gradient(90deg, var(--band-red-light), var(--band-red) 60%, var(--band-red-light)); }
  .title { position: absolute; left: 26px; top: 12px; color: var(--white); font-weight: 500;
    font-size: 43px; letter-spacing: -0.5px; line-height: 48px; }
  .copy { position: absolute; left: 228px; top: 198px; width: 414px; color: var(--body-text);
    font-weight: 300; font-size: 24px; line-height: 32.2px; letter-spacing: 1px; text-align: justify; }
  .copy p + p { margin-top: 58px; }
  .divider { position: absolute; left: 679px; top: 207px; height: 483px; border-left: 1px dashed var(--divider); }
  .chart { position: absolute; left: 0; top: 0; }
  .pct { font-family: "Barlow", Arial, sans-serif; font-size: 18px; fill: #222; }
  .core-label { font-family: "Barlow", Arial, sans-serif; font-size: 21px; fill: var(--label); }
</style>
</head>
<body>
<div class="slide">
  <div class="sidebar">
    <div class="brand"><span class="brand-mark"></span>TESSEL7</div>
  </div>
  <div class="band-tab"></div>
  <div class="title-band"><h1 class="title">STRATEGY AND OUR VISION</h1></div>
  <div class="band-fold"></div>

  <div class="copy">
    <p>Tessel7 delivers broad industry experience to your project. Our combined talent and years of experience in enterprise software deployment can help you get better value from your technology investment.</p>
    <p>Smaller team and focused attention means you see efficient and effective results. We use the latest technology to streamline our own operations for cost effective performance.</p>
  </div>

  <div class="divider"></div>

  <svg class="chart" width="1200" height="900" viewBox="0 0 1200 900" aria-label="Web Experience Management chart: three equal parts of 33%">
    <path d="M949 452 L949 254 A198 198 0 0 1 1120.5 551 Z" fill="var(--navy)"/>
    <path d="M949 452 L1120.5 551 A198 198 0 0 1 777.5 551 Z" fill="var(--coral)"/>
    <path d="M949 452 L777.5 551 A198 198 0 0 1 949 254 Z" fill="var(--olive)"/>
    <circle cx="949" cy="452" r="150" fill="#ffffff" fill-opacity="0.38"/>
    <circle cx="949" cy="452" r="146" fill="none" stroke="#ffffff" stroke-opacity="0.7" stroke-width="1.5"/>
    <circle cx="949" cy="452" r="130" fill="none" stroke="#ffffff" stroke-opacity="0.6" stroke-width="1"/>
    <polygon fill="var(--core)" points="949,332 980.5,355 1019.6,354.9 1031.5,392 1063.1,414.9 1051,452 1063.1,489.1 1031.5,512 1019.6,549.1 980.5,549 949,572 917.5,549 878.4,549.1 866.5,512 834.9,489.1 847,452 834.9,414.9 866.5,392 878.4,354.9 917.5,355"/>
    <text class="core-label" x="949" y="444" text-anchor="middle">Web Experience</text>
    <text class="core-label" x="949" y="472" text-anchor="middle">Management</text>
    <text class="pct" x="1124" y="307">33%</text>
    <text class="pct" x="725" y="344">33%</text>
    <text class="pct" x="761" y="628">33%</text>
  </svg>
</div>
</body>
</html>
```